International MLM Business needs Coffee Packaging Design

We are an MLM Company engaged in selling Food Supplements to our independent distributors.

We need a Packaging Design for our Instant Coffee (Cafe Latte) enhanced with Food Supplement (Ganoderma and Goji Powder)

Sachet Material is PET/AL/PE
Sachet Size is 45mm x 160mm (L x H) (FORMED)
Canvass Size is 110mm x 160mm (L x H) (FLAT)

The packaging design requirements are as follows:

1. Design must be in upright position (portrait).

2. We would like to see "VELTORIS" (our brand logo) included in the design. See uploaded file.

3. We also would like to see some "gold" touch in the label.

4. The coffee is part of our "SUPER" series.

5. Include "PREMIUM COFFEE", "WITH GANODERMA & GOJI EXTRACT" as our main selling point.

6. Add Net Weight at the lower right portion. Net Weight is 25 grams.

7. Add Serving Instruction at the Back.

1. Empty 1 sachet of VELTORIS Prime Brew Latte into a mug.
2. Fill the mug with 220ml of hot water (80 degrees celsius) and stir. (Use "80oc")
I don't know how to superscript the "o".
3. Enjoy a rich, healthy VELTORIS Prime Brew Latte.

8. Add Ingredients at the Back.

"Sugar, Non Dairy Creamer, Pure Instant Coffee, Organic Goji Extract, Organic Ganoderma Extract."

9. Add Best Before Date at the Back.

10. Add Manufacturer Details at the Back.

Our website is http://www.veltoris-example.com

*attached photo is for presentation purposes only. It's up to you to design.*

Designer Payment changed to committed. We are very serious about this project. So please kindly submit all entries. Thanks!

```html
<!DOCTYPE html>
<html lang="en">
<head>
<meta charset="utf-8">
<title>VELTORIS Prime Brew Latte – Sachet Flat</title>
<link rel="stylesheet" href="https://fonts.googleapis.com/css2?family=Nunito:wght@600&family=Open+Sans:wght@600;700;800&family=Roboto+Condensed:wght@400;700&display=swap">
<style>
  :root {
    --bg: #eeeeee;
    --brown: #7a5230;
    --brown-dark: #5e3c20;
    --brown-light: #936640;
    --cream: #f7f3a6;
    --gold: #f3c21a;
    --gold-light: #fde27a;
    --gold-dark: #c98f0c;
    --wine: #8a1c0c;
    --green: #4f9a2a;
    --white: #ffffff;
  }
  * { box-sizing: border-box; margin: 0; padding: 0; }
  html, body { width: 1200px; height: 1200px; overflow: hidden; }
  body { background: var(--bg); font-family: "Roboto Condensed", Arial, sans-serif; }

  .sachet {
    position: absolute; left: 220px; top: 50px; width: 760px; height: 1100px;
    background: var(--brown); overflow: hidden;
    box-shadow: 0 10px 30px rgba(0,0,0,.18);
  }
  .seal {
    position: absolute; left: 0; width: 100%; height: 45px; z-index: 5;
    background: repeating-linear-gradient(90deg, var(--brown-dark) 0 3px, var(--brown) 3px 12px);
  }
  .seal--top { top: 0; }
  .seal--bottom { bottom: 0; }
  .fin-line { position: absolute; top: 45px; bottom: 45px; width: 2px; background: var(--brown-light); }

  /* front panel */
  .front { position: absolute; left: 230px; top: 0; width: 315px; height: 100%; }
  .front__header { position: absolute; left: 0; top: 0; width: 100%; height: 250px; }
  .brand {
    position: absolute; top: 95px; left: 0; width: 100%;
    display: flex; flex-direction: column; align-items: center; gap: 8px;
  }
  .brand__dot { width: 44px; height: 44px; border-radius: 50%; background: var(--green); }
  .brand__name { font-family: "Nunito", sans-serif; font-weight: 600; font-size: 22px; color: var(--green); }
  .title { position: absolute; top: 275px; left: 0; width: 100%; text-align: center; }
  .title__main {
    font-family: "Open Sans", sans-serif; font-weight: 800; font-size: 50px;
    color: var(--gold-light); line-height: 1; letter-spacing: 1px;
  }
  .title__sub {
    font-family: "Open Sans", sans-serif; font-weight: 600; font-size: 30px;
    color: var(--white); line-height: 1.2; margin-top: 8px; letter-spacing: 2px;
  }
  .title__rule { width: 220px; height: 4px; margin: 10px auto 0; background: linear-gradient(90deg, transparent, var(--gold), transparent); }
  .front__photo {
    position: absolute; left: 0; top: 450px; width: 100%; height: 440px;
    background: radial-gradient(ellipse at 50% 35%, #e8c689 0 30%, #f4efe6 42%, #d8cfc4 60%, #8c4a2a 80%, var(--brown) 100%);
  }
  .selling {
    position: absolute; left: -10px; top: 880px; width: 335px; height: 120px;
    background: linear-gradient(180deg, var(--gold-light), var(--gold) 45%, var(--gold-dark));
    transform: skewY(-4deg);
    display: flex; align-items: center; justify-content: center;
  }
  .selling__text {
    transform: skewY(4deg); text-align: center;
    font-family: "Open Sans", sans-serif; font-weight: 800; font-size: 24px;
    line-height: 1.2; color: var(--wine);
  }
  .net-weight {
    position: absolute; right: 16px; bottom: 56px;
    font-family: "Open Sans", sans-serif; font-weight: 700; font-size: 17px; color: var(--white);
  }

  /* rotated side panels */
  .side { position: absolute; top: 45px; height: 1010px; }
  .side__inner {
    position: absolute; left: 50%; top: 50%; width: 1010px;
    transform: translate(-50%, -50%) rotate(-90deg);
    color: var(--white);
  }
  .side--left { left: 0; width: 230px; }
  .side--left .side__inner { height: 230px; }
  .side--back { left: 545px; width: 215px; }
  .side--back .side__inner { height: 215px; }

  .maker { position: absolute; right: 40px; top: 22px; width: 520px; font-size: 14px; line-height: 1.35; }
  .maker__brand { position: absolute; right: 40px; top: 110px; display: flex; align-items: center; gap: 8px; font-family: "Nunito", sans-serif; font-weight: 600; font-size: 16px; }
  .maker__dot { width: 16px; height: 16px; border-radius: 50%; background: var(--white); }
  .storage { position: absolute; left: 60px; top: 22px; font-size: 15px; line-height: 2.4; }

  .back__heading { position: absolute; left: 230px; top: 16px; font-size: 27px; font-weight: 700; color: var(--gold); white-space: nowrap; }
  .steps { position: absolute; left: 230px; top: 60px; width: 480px; font-size: 15px; line-height: 1.5; list-style: none; }
  .steps li::before { content: "\25CF"; font-size: 10px; margin-right: 8px; vertical-align: 2px; }
  .ingredients {
    position: absolute; right: 26px; top: 60px; width: 250px;
    border: 1px solid var(--gold-light); border-radius: 8px; padding: 8px 12px;
    font-size: 13.5px; line-height: 1.3;
  }
  .ingredients__label { font-weight: 700; }
  .back__photo {
    position: absolute; left: 24px; top: 40px; width: 170px; height: 150px; border-radius: 6px;
    background: radial-gradient(ellipse at 45% 45%, #e8c689 0 25%, #f4efe6 40%, #cfc5b8 62%, var(--brown) 80%);
  }
</style>
</head>
<body>
<main class="sachet" aria-label="VELTORIS Prime Brew Latte sachet, flat artwork">
  <div class="seal seal--top"></div>
  <div class="seal seal--bottom"></div>
  <div class="fin-line" style="left:36px"></div>
  <div class="fin-line" style="left:206px"></div>

  <section class="side side--left">
    <div class="side__inner">
      <p class="storage">Best Before Date:<br><br>Store in cool and dry place</p>
      <p class="maker">Exclusively Manufactured for and Distributed By:<br>Unit 4 3rd flr. Halden Crest Tower, Marlow Avenue,<br>Larkspur Center, Eastvale City, 1600<br>www.veltoris-example.com</p>
      <div class="maker__brand"><span class="maker__dot"></span>veltoris-example</div>
    </div>
  </section>

  <section class="front">
    <svg class="front__header" viewBox="0 0 315 250" preserveAspectRatio="none">
      <path d="M0 0H315V175C250 215 170 180 110 200C60 215 25 235 0 240Z" fill="var(--cream)"/>
      <path d="M0 240C25 235 60 215 110 200C170 180 250 215 315 175V182C250 222 170 188 110 208C60 224 25 243 0 248Z" fill="var(--gold)"/>
    </svg>
    <div class="brand">
      <span class="brand__dot"></span>
      <span class="brand__name">veltoris-example</span>
    </div>
    <div class="title">
      <div class="title__main">PRIME</div>
      <div class="title__sub">Brew Latte</div>
      <div class="title__rule"></div>
    </div>
    <div class="front__photo" role="img" aria-label="Cup of latte on a saucer with ganoderma mushroom and goji berries"></div>
    <div class="selling">
      <p class="selling__text">Premium Coffee<br>With Ganoderma<br>&amp; Goji Extract</p>
    </div>
    <p class="net-weight">Net Weight: 25g</p>
  </section>

  <section class="side side--back">
    <div class="side__inner">
      <div class="back__photo" role="img" aria-label="Small cup of latte with ganoderma and goji berries"></div>
      <h2 class="back__heading">Premium Coffee With Ganoderma &amp; Goji Extract</h2>
      <ul class="steps">
        <li>Empty 1 sachet of VELTORIS Prime Brew Latte into a mug.</li>
        <li>Fill the mug with 220ml of hot water (80<sup>o</sup>C) and stir.</li>
        <li>Enjoy a rich, healthy VELTORIS Prime Brew Latte.</li>
      </ul>
      <div class="ingredients">
        <span class="ingredients__label">Ingredients:</span><br>
        Sugar, Non Dairy Creamer, Pure Instant Coffee, Organic Goji Extract, Organic Ganoderma Extract.
      </div>
    </div>
  </section>
</main>
</body>
</html>
```